Country Duo act needs single artwork

We need artwork for our latest single for quavera and other music streaming sites. The design can include the pictures in the attached files that we uploaded but we are also open to designs that also don't include them. It should be easy to read the song title
"Rain Keeps Turning" and our band name Harbor 82 - this track is our actual story. Must be at least 640 x 640 pixels to be acceptable to quavera. We have also included a copy of the track for inspiration.
Check us out on quavera to see other artwork -> https://open.quavera-tunes.example/artist/4kTqZbN7rW2mLxPd9HsVyE?si=Hc8Jw2TnQpLm5VaRkXbYzG

Target Market(s)

Country music fans

Industry/Entity Type

Music

Font styles to use
Decorative

Colors

Designer to choose colors to be used in the design.

Requirements
Must have
• Name of song Title and band name
Nice to have
• Vibe that matches the song / one of our pictures included
Should not have
• any other text

```html
<!DOCTYPE html>
<html lang="en">
<head>
<meta charset="UTF-8">
<title>Harbor 82 – Rain Keeps Turning</title>
<link href="https://fonts.googleapis.com/css2?family=Oswald:wght@600&family=Kaushan+Script&display=swap" rel="stylesheet">
<style>
  :root {
    --ink-white: #fbf8f2;
    --band-white: #f3ede2;
    --shadow-dark: #120d08;
    --glow-amber: #c8741f;
    --bg-deep: #1a140c;
    --bg-olive: #2c2a18;
    --bg-brown: #3a2614;
  }
  html, body {
    margin: 0;
    padding: 0;
    width: 1200px;
    height: 1200px;
    overflow: hidden;
    background: var(--bg-deep);
  }
  .cover {
    position: relative;
    width: 1200px;
    height: 1200px;
    overflow: hidden;
  }
  .duo-photo {
    position: absolute;
    inset: 0;
    background:
      radial-gradient(ellipse 55% 30% at 50% 18%, rgba(200,116,31,0.85), rgba(200,116,31,0) 70%),
      radial-gradient(ellipse 45% 55% at 50% 65%, #4a3a2c 0%, rgba(74,58,44,0) 75%),
      linear-gradient(180deg, var(--bg-brown) 0%, var(--bg-deep) 40%, var(--bg-olive) 80%, #1d2118 100%);
  }
  .band-name {
    position: absolute;
    top: 30px;
    left: 0;
    width: 1200px;
    margin: 0;
    text-align: center;
    font-family: "Oswald", sans-serif;
    font-weight: 600;
    font-size: 200px;
    line-height: 1.2;
    letter-spacing: 14px;
    text-transform: uppercase;
    color: var(--band-white);
    white-space: nowrap;
  }
  .song-title {
    position: absolute;
    inset: 0;
    margin: 0;
    font-family: "Kaushan Script", cursive;
    font-weight: 400;
    color: var(--ink-white);
    transform: rotate(-4deg);
    transform-origin: 600px 800px;
  }
  .song-title span {
    position: absolute;
    white-space: nowrap;
    line-height: 1;
    font-size: 200px;
    -webkit-text-stroke: 3px var(--shadow-dark);
    paint-order: stroke fill;
    text-shadow: 6px 6px 0 var(--shadow-dark);
  }
  .title-word-1 { left: 140px; top: 420px; }
  .title-word-2 { left: 450px; top: 650px; }
  .title-word-3 { left: 170px; top: 880px; }
</style>
</head>
<body>
  <main class="cover">
    <div class="duo-photo" role="img" aria-label="Photo of the country duo sitting close together outdoors, heads leaning in, warm evening light behind them"></div>
    <h1 class="band-name">Harbor 82</h1>
    <h2 class="song-title">
      <span class="title-word-1">Rain</span>
      <span class="title-word-2">Keeps</span>
      <span class="title-word-3">Turning</span>
    </h2>
  </main>
</body>
</html>
```